Discreet simple classy for adult entertainment

I would like a matte black business card with gold writing for my business. Keeping it simple. Having my following:

Lana frost
Events. Entertainment. Promotions
0491726580

or alternatively could have what i had on my previous card below but i think i prefer the above as again - discretion.

Maybe a nice gold line thru the card or some other very simple design . Or not open to ideas/ can be doublesided if any good ideas with that.

included pics of my old bus card. not sure weather i want a photo on it or not. if i do it wont be the same pic. i kinda wanted a card that was discreet so if it was in someones wallet they wouldn't neccessarily realise it was from a stripper.

Target Market(s)

men

Industry/Entity Type

Business

Contact Information for Business Card

Lana frost
0491726580

Requirements
Nice to have
• i don't know i am really open to anything. im giving my cards to guys so something they can have in their wallet that is discreet preferably.

```html
<!DOCTYPE html>
<html lang="en">
<head>
<meta charset="utf-8">
<title>Lana Frost – Business Card</title>
<link rel="stylesheet" href="https://fonts.googleapis.com/css2?family=Open+Sans:wght@400;700&display=swap">
<style>
  :root {
    --backdrop: #e4ddd3;
    --card-black: #161616;
    --gold: #b47c3e;
    --gold-line: #8a5e2e;
    --gold-fine: #6e4b26;
    --stripe-tone: #2b2219;
  }
  * { margin: 0; padding: 0; box-sizing: border-box; }
  html, body {
    width: 1200px;
    height: 815px;
    overflow: hidden;
    background: var(--backdrop);
    font-family: "Open Sans", Arial, sans-serif;
  }
  .sheet {
    position: relative;
    width: 1200px;
    height: 815px;
  }
  .card {
    position: absolute;
    top: 245px;
    width: 520px;
    height: 325px;
    background: var(--card-black);
    border-radius: 22px;
  }
  .card--back { left: 50px; }
  .card--front { left: 630px; }
  .card__frame {
    position: absolute;
    inset: 15px;
    border: 1.5px solid var(--gold-line);
    border-radius: 18px;
  }
  .accent-band {
    position: absolute;
    top: 132px;
    width: 108px;
    height: 50px;
    background: linear-gradient(90deg, rgba(43,34,25,0.6), var(--stripe-tone) 30%, var(--stripe-tone) 70%, rgba(43,34,25,0.6));
  }
  .accent-band--left { left: 50px; }
  .accent-band--right { left: 362px; }
  .card__rules {
    position: absolute;
    left: 0;
    top: 0;
    width: 520px;
    height: 325px;
  }
  .services {
    position: absolute;
    left: 0;
    right: 0;
    top: 126px;
    text-align: center;
    color: var(--gold);
    font-size: 19px;
    line-height: 23px;
    letter-spacing: 0.5px;
  }
  .holder-name {
    position: absolute;
    left: 0;
    right: 0;
    top: 104px;
    text-align: center;
    color: var(--gold);
    font-weight: 700;
    font-size: 38px;
    letter-spacing: 2px;
  }
  .holder-phone {
    position: absolute;
    left: 0;
    right: 0;
    top: 186px;
    text-align: center;
    color: var(--gold-line);
    font-size: 21px;
    letter-spacing: 1px;
  }
</style>
</head>
<body>
<main class="sheet">
  <section class="card card--back" aria-label="Card back">
    <div class="card__frame"></div>
    <div class="accent-band accent-band--left" role="img" aria-label="Fine gold striped accent panel"></div>
    <div class="accent-band accent-band--right" role="img" aria-label="Fine gold striped accent panel"></div>
    <p class="services">Events<br>Entertainment<br>Promotions</p>
  </section>

  <section class="card card--front" aria-label="Card front">
    <div class="card__frame"></div>
    <svg class="card__rules" viewBox="0 0 520 325" aria-hidden="true">
      <g stroke="var(--gold-fine)" stroke-width="1">
        <line x1="45" y1="199" x2="178" y2="199"/>
        <line x1="342" y1="199" x2="475" y2="199"/>
      </g>
    </svg>
    <h1 class="holder-name">LANA FROST</h1>
    <p class="holder-phone">0491726580</p>
  </section>
</main>
</body>
</html>
```